App Design for Restaurant App

We need a design for the new Mobile App for the Restaurant Volmik. See attachment for presentation sketches.
There are two attached files: File 2 shows the App in general and File 1 shows the five screens which need to be designed. Your work should contain the general color scheme, icons and layout proposal.
Updates
Hi Designers
There where several questions about the scope of the work. We are looking for a design for an App. The promotion website of the restaurant Volmik can be found under www.restaurant-volmik.ch
There you will get an impression of the Corporate Identity used by the restaurant and you will also find the logo.
In the sketch there are several screens which don't need a design, e.g. the cover flow or video screen
please ask if you have any question
kind regards
Tobias
Industry/Entity Type
Restaurant
Look and feel
Each slider illustrates characteristics of the customer's brand and the style your logo design should communicate.

```html
<!DOCTYPE html>
<html lang="de">
<head>
<meta charset="utf-8">
<title>Restaurant Volmik – App</title>
<link rel="stylesheet" href="https://fonts.googleapis.com/css2?family=Oswald:wght@600&family=Ubuntu:wght@400&display=swap">
<style>
  :root {
    --bg: #5e6e61;
    --tile: #6a7e6e;
    --frame: #f4f6f4;
    --icon: #eceeed;
    --icon-detail: #6f8273;
    --label: #ffffff;
    --accent-a: #2fd0d6;
    --accent-b: #6fa58a;
    --header-a: #0f5a3c;
    --header-b: #2fb079;
    --header-c: #b9f0d2;
  }
  * { box-sizing: border-box; margin: 0; padding: 0; }
  html, body { width: 800px; height: 1200px; overflow: hidden; background: var(--bg); }
  .app-screen { position: relative; width: 800px; height: 1200px; background: var(--bg); }
  .app-header {
    position: absolute; left: 20px; top: 20px; width: 760px; height: 320px;
    border: 8px solid var(--frame);
    background:
      linear-gradient(160deg, rgba(255,255,255,0.0) 40%, rgba(200,255,230,0.35) 62%, rgba(255,255,255,0) 80%),
      linear-gradient(115deg, var(--header-a) 0%, var(--header-b) 45%, var(--header-c) 70%, var(--header-b) 85%, var(--header-a) 100%);
    display: flex; align-items: center; justify-content: center;
  }
  .app-title {
    font-family: "Oswald", sans-serif; font-weight: 600; font-size: 78px;
    color: #ffffff; letter-spacing: 1px; line-height: 1;
  }
  .menu-grid {
    position: absolute; left: 20px; top: 365px; width: 760px;
    display: grid; grid-template-columns: repeat(3, 240px); grid-auto-rows: 260px;
    column-gap: 20px; row-gap: 20px;
  }
  .menu-tile {
    position: relative; border: 7px solid var(--frame); background: var(--tile);
    display: flex; flex-direction: column; align-items: center;
  }
  .menu-tile.is-active { background: linear-gradient(135deg, var(--accent-a) 0%, var(--accent-b) 75%); }
  .menu-icon { width: 120px; height: 120px; margin-top: 34px; }
  .menu-label {
    position: absolute; bottom: 18px; left: 0; right: 0; text-align: center;
    font-family: "Ubuntu", sans-serif; font-size: 34px; color: var(--label);
  }
  .ic { fill: var(--icon); }
  .ic-d { fill: var(--icon-detail); }
  .ic-s { stroke: var(--icon-detail); fill: none; }
</style>
</head>
<body>
<main class="app-screen">
  <header class="app-header" role="img" aria-label="Abstrakte grüne Lichtstreifen als Kopfbild">
    <h1 class="app-title">RESTAURANTVOLMIK</h1>
  </header>

  <nav class="menu-grid">
    <a class="menu-tile is-active">
      <svg class="menu-icon" viewBox="0 0 100 100"><circle class="ic" cx="50" cy="50" r="40"/><circle class="ic-d" cx="52" cy="30" r="6"/><path class="ic-d" d="M44 42h14l-6 30h6v5H40v-5h5z"/></svg>
      <span class="menu-label">info</span>
    </a>
    <a class="menu-tile">
      <svg class="menu-icon" viewBox="0 0 100 100"><path class="ic" d="M6 50C20 28 36 20 50 20s30 8 44 30C80 72 64 80 50 80S20 72 6 50z"/><circle class="ic-d" cx="50" cy="50" r="17"/><circle class="ic" cx="44" cy="44" r="5"/></svg>
      <span class="menu-label">webcam</span>
    </a>
    <a class="menu-tile">
      <svg class="menu-icon" viewBox="0 0 100 100"><path class="ic" d="M50 12 8 52h12v36h22V64h16v24h22V52h12L74 29V16H64v4z"/></svg>
      <span class="menu-label">restourant</span>
    </a>
    <a class="menu-tile">
      <svg class="menu-icon" viewBox="0 0 100 100"><path class="ic" d="M38 10h26v6l-5 4v22l12 10v6H53L44 92h-2l2-34H31v-6l12-10V20l-5-4z"/></svg>
      <span class="menu-label">events</span>
    </a>
    <a class="menu-tile">
      <svg class="menu-icon" viewBox="0 0 100 100"><rect class="ic" x="12" y="16" width="76" height="72" rx="8"/><rect class="ic-d" x="12" y="16" width="76" height="6"/><rect class="ic-d" x="26" y="8" width="6" height="16" rx="3"/><rect class="ic-d" x="68" y="8" width="6" height="16" rx="3"/><g class="ic-d"><rect x="20" y="32" width="12" height="10"/><rect x="36" y="32" width="12" height="10"/><rect x="52" y="32" width="12" height="10"/><rect x="68" y="32" width="12" height="10"/><rect x="20" y="48" width="12" height="10"/><rect x="36" y="48" width="12" height="10"/><rect x="52" y="48" width="12" height="10"/><rect x="68" y="48" width="12" height="10"/><rect x="20" y="64" width="12" height="10"/><rect x="36" y="64" width="12" height="10"/><rect x="52" y="64" width="12" height="10"/><rect x="68" y="64" width="12" height="10"/></g></svg>
      <span class="menu-label">reservation</span>
    </a>
    <a class="menu-tile">
      <svg class="menu-icon" viewBox="0 0 100 100"><circle class="ic" cx="50" cy="50" r="42"/><path class="ic-d" d="M34 22h3v14h2V22h3v14h2V22h3v18c0 4-3 6-5 6v32h-6V46c-2 0-5-2-5-6z"/><path class="ic-d" d="M60 22c6 0 9 8 9 20 0 5-2 7-4 8v28h-6z"/></svg>
      <span class="menu-label">menukarte</span>
    </a>
    <a class="menu-tile">
      <svg class="menu-icon" viewBox="0 0 100 100"><path class="ic" d="M10 30h20l6-10h28l6 10h20v54H10z"/><circle class="ic-d" cx="50" cy="56" r="18"/><circle class="ic" cx="50" cy="56" r="11"/><rect class="ic-d" x="14" y="22" width="10" height="5"/></svg>
      <span class="menu-label">galarie</span>
    </a>
    <a class="menu-tile">
      <svg class="menu-icon" viewBox="0 0 100 100"><path class="ic" d="M8 54 92 16 60 86 48 62z"/><path class="ic-d" d="M48 62 92 16 54 60z" opacity="0.45"/></svg>
      <span class="menu-label">anfahrt</span>
    </a>
    <a class="menu-tile">
      <svg class="menu-icon" viewBox="0 0 100 100"><rect class="ic" x="18" y="10" width="64" height="80" rx="4"/><rect class="ic-d" x="22" y="10" width="4" height="80"/><path class="ic-d" d="M56 10h14v30l-7-6-7 6z"/></svg>
      <span class="menu-label">gastebuch</span>
    </a>
  </nav>
</main>
</body>
</html>
```